Varotesk with two other company logos

We need a new design for our business cards. We have used the same business cards for more than 10 years. We have now expanded and want to add our other two business logos to incorporate with our original business logo. I have added our current business card (Varotesk) onto here. Also I have added an example of what we would like to see on the business card.

Target Market(s)

Nutritional market

Industry/Entity Type

Business

Contact Information for Business Card

Varotesk, Hallinger Product Plant, Brisk lift Product
Will use business cards for Multiple of people in my company.

Colors

Designer to choose colors to be used in the design.

Requirements
Must have
• three logos on my business cards
Nice to have
• something that stands out.

```html
<!DOCTYPE html>
<html lang="en">
<head>
<meta charset="utf-8">
<title>Business Cards</title>
<link rel="stylesheet" href="https://fonts.googleapis.com/css2?family=Montserrat:wght@700&family=Open+Sans:wght@400;700&display=swap">
<style>
  :root {
    --stage: #6b6b6b;
    --card: #f1f1f0;
    --navy: #1f2f7a;
    --green: #7aa866;
    --grey-text: #6a6a6a;
    --rule: #8a8a8a;
    --faint: #e2e5ee;
  }
  * { margin: 0; padding: 0; box-sizing: border-box; }
  html, body { width: 1200px; height: 904px; overflow: hidden; }
  body {
    background: var(--stage);
    font-family: "Open Sans", sans-serif;
    position: relative;
  }
  .card {
    position: absolute;
    left: 290px;
    width: 620px;
    height: 354px;
    background: var(--card);
    border-radius: 3px;
    box-shadow: 0 6px 18px rgba(0,0,0,.35);
    overflow: hidden;
  }
  .card--brand { top: 68px; }
  .card--contact { top: 482px; }

  /* Front card */
  .brand-backdrop {
    position: absolute;
    left: 40px;
    top: 40px;
    width: 270px;
    height: 270px;
    border-radius: 50%;
    background: var(--faint);
  }
  .brand-stack {
    position: absolute;
    right: 40px;
    top: 70px;
    width: 250px;
    display: flex;
    flex-direction: column;
    align-items: center;
    gap: 34px;
  }
  .brand-mark {
    display: flex;
    flex-direction: column;
    align-items: center;
    gap: 10px;
    text-align: center;
  }
  .brand-mark__dot {
    width: 30px; height: 30px; border-radius: 50%;
    background: var(--green);
  }
  .brand-mark__name {
    font-family: "Montserrat", sans-serif;
    font-weight: 700;
    font-size: 24px;
    line-height: 1.15;
    color: var(--green);
  }
  .brand-mark--parent .brand-mark__dot {
    border-radius: 0;
    width: 22px; height: 22px;
    background: var(--navy);
  }
  .brand-mark--parent .brand-mark__name {
    color: var(--navy);
    font-size: 22px;
  }

  /* Back card */
  .company-mark {
    position: absolute;
    left: 0;
    right: 0;
    top: 70px;
    display: flex;
    justify-content: center;
    align-items: center;
    gap: 12px;
  }
  .company-mark__dot {
    width: 40px; height: 40px; border-radius: 50%;
    background: var(--navy);
  }
  .company-mark__name {
    font-family: "Montserrat", sans-serif;
    font-weight: 700;
    font-size: 25px;
    color: var(--navy);
    text-transform: uppercase;
  }

  .divider {
    position: absolute;
    left: 350px;
    top: 178px;
    width: 1px;
    height: 118px;
    background: var(--rule);
  }
  .person {
    position: absolute;
    right: 290px;
    top: 242px;
    text-align right;
    text-align: right;
  }
  .person__name { font-weight: 700; font-size: 22px; color: var(--navy); }
  .person__title { font-size: 15px; color: var(--grey-text); }

  .contact {
    position: absolute;
    left: 372px;
    top: 176px;
    font-size: 15px;
    line-height: 21px;
    color: var(--grey-text);
    list-style: none;
  }
  .contact__item { display: flex; align-items: center; gap: 10px; }
  .contact__icon { width: 14px; height: 14px; flex: none; }
</style>
</head>
<body>

<section class="card card--brand">
  <div class="brand-backdrop" role="img" aria-label="Large faint brand circle decoration"></div>
  <div class="brand-stack">
    <div class="brand-mark">
      <span class="brand-mark__dot"></span>
      <span class="brand-mark__name">Hallinger<br>Product Plant</span>
    </div>
    <div class="brand-mark brand-mark--parent">
      <span class="brand-mark__dot"></span>
      <span class="brand-mark__name">Varotesk</span>
    </div>
  </div>
</section>

<section class="card card--contact">
  <div class="company-mark">
    <span class="company-mark__dot"></span>
    <span class="company-mark__name">Brisk lift Product</span>
  </div>

  <div class="person">
    <p class="person__name">Dana Whitfield</p>
    <p class="person__title">President / Owner</p>
  </div>

  <div class="divider"></div>

  <ul class="contact">
    <li class="contact__item">P.O. Box 418</li>
    <li class="contact__item">Elm Ridge, WI 53190</li>
    <li class="contact__item">
      <svg class="contact__icon" viewBox="0 0 24 24" aria-hidden="true"><circle cx="12" cy="12" r="12" fill="#1f2f7a"/><path d="M8 6l2 0 1 3-1.5 1c.8 1.8 2 3 3.5 3.5l1-1.5 3 1v2c0 1-1 1.5-2 1.5C10 16.5 7.5 14 7 8c0-1 .5-2 1-2z" fill="#fff"/></svg>
      555-014-2233
    </li>
    <li class="contact__item">
      <svg class="contact__icon" viewBox="0 0 24 24" aria-hidden="true"><circle cx="12" cy="12" r="12" fill="#1f2f7a"/><rect x="6" y="10" width="12" height="6" fill="#fff"/><rect x="8" y="6" width="8" height="4" fill="#fff"/><rect x="8" y="14" width="8" height="4" fill="#1f2f7a" stroke="#fff"/></svg>
      555-014-7788
    </li>
    <li class="contact__item">
      <svg class="contact__icon" viewBox="0 0 24 24" aria-hidden="true"><circle cx="12" cy="12" r="12" fill="#1f2f7a"/><rect x="6" y="8" width="12" height="8" fill="#fff"/><path d="M6 8l6 5 6-5" fill="none" stroke="#1f2f7a" stroke-width="1.2"/></svg>
      dana@varotesk.com
    </li>
    <li class="contact__item">
      <svg class="contact__icon" viewBox="0 0 24 24" aria-hidden="true"><circle cx="12" cy="12" r="12" fill="#1f2f7a"/><circle cx="12" cy="12" r="6" fill="none" stroke="#fff" stroke-width="1.3"/><path d="M6 12h12M12 6c-3 3-3 9 0 12M12 6c3 3 3 9 0 12" fill="none" stroke="#fff" stroke-width="1.1"/></svg>
      www.varotesk.com
    </li>
  </ul>
</section>

</body>
</html>
```